Simple : A Therapist is looking for a Design

Im lookind for a business card design for my new business .
my therapy field - Attuned Somatic Release .
Its part of Osteopatic medicine .
its gental, not invasive method that focus on the bones of the skull (cranial) .
i want some kind of skull in it like the attached photo.

Target Market(s)

people that suffer from pain

Industry/Entity Type

Physical Therapy

Contact Information for Business Card

i want people to understand this is diffrent kind of therapy
its anatomy base , gental and give outstanding result .

Font styles to use
Serif

Colors
fee18a
cadf82
fbc994
cedeed
fbe7d2
fff3d1

Requirements
Must have
• one side: my name (Eliran Tsabari) ,
• phone number ( 0541762908)
• email (tsabarieliran@mailvent.net)
• other side : Attuned Somatic Release
Nice to have
• i want some kind of skull in it like the attached photo.
• very powrful, accurate and smart.
• nice colores (maybe lite orange?, lite green?) , simple, relax, smart

```html
<!DOCTYPE html>
<html lang="en">
<head>
<meta charset="utf-8">
<title>Attuned Somatic Release – Business Card</title>
<link href="https://fonts.googleapis.com/css2?family=Exo+2:wght@400&display=swap" rel="stylesheet">
<style>
  :root {
    --page-bg: #2b2b2b;
    --card-front: #fbe28f;
    --card-back: #ffffff;
    --brand-text: #ffffff;
    --name-green: #bcd873;
    --contact-yellow: #f0d27a;
    --soft-cream: #fff3d1;
  }
  * { box-sizing: border-box; margin: 0; padding: 0; }
  html, body {
    width: 1200px;
    height: 880px;
    overflow: hidden;
    background: var(--page-bg);
    font-family: "Exo 2", sans-serif;
  }
  .canvas {
    position: relative;
    width: 1200px;
    height: 880px;
  }
  .card {
    position: absolute;
    left: 320px;
    width: 560px;
    height: 320px;
    border-radius: 26px;
    overflow: hidden;
    box-shadow: 0 10px 30px rgba(0, 0, 0, 0.45);
  }
  .card--front {
    top: 60px;
    background: var(--card-front);
  }
  .card--back {
    top: 480px;
    background: var(--card-back);
  }
  .brand {
    position: absolute;
    left: 170px;
    top: 118px;
    display: flex;
    align-items: center;
    gap: 14px;
    color: var(--brand-text);
    font-weight: 400;
  }
  .brand__mark {
    width: 18px;
    height: 18px;
    border-radius: 50%;
    background: var(--brand-text);
    flex: none;
  }
  .brand__name {
    line-height: 1;
  }
  .brand__line1 {
    display: block;
    font-size: 44px;
    letter-spacing: 1px;
  }
  .brand__line2 {
    display: block;
    font-size: 26px;
    letter-spacing: 3px;
    margin-top: 4px;
  }
  .back-decoration {
    position: absolute;
    left: 110px;
    top: 40px;
    width: 420px;
    height: 120px;
    border-radius: 60px;
    background: radial-gradient(ellipse at center, var(--soft-cream) 0%, rgba(255, 243, 209, 0) 72%);
  }
  .contact {
    position: absolute;
    left: 36px;
    bottom: 34px;
  }
  .contact__name {
    color: var(--name-green);
    font-size: 22px;
    letter-spacing: 0.5px;
    margin-bottom: 8px;
  }
  .contact__row {
    display: flex;
    align-items: center;
    gap: 8px;
    color: var(--contact-yellow);
    font-size: 15px;
    line-height: 1.5;
    letter-spacing: 0.5px;
  }
  .contact__icon {
    width: 14px;
    height: 14px;
    flex: none;
  }
</style>
</head>
<body>
<main class="canvas">
  <section class="card card--front" aria-label="Card front">
    <div class="brand">
      <span class="brand__mark"></span>
      <p class="brand__name">
        <span class="brand__line1">Attuned</span>
        <span class="brand__line2">Somatic Release</span>
      </p>
    </div>
  </section>

  <section class="card card--back" aria-label="Card back">
    <div class="back-decoration" role="img" aria-label="Faint cream decorative background band"></div>
    <div class="contact">
      <p class="contact__name">Eliran Tsabari</p>
      <p class="contact__row">
        <svg class="contact__icon" viewBox="0 0 14 14" aria-hidden="true">
          <rect x="3" y="1" width="8" height="12" rx="1.5" fill="none" stroke="var(--name-green)" stroke-width="1.4"/>
          <line x1="6" y1="11" x2="8" y2="11" stroke="var(--name-green)" stroke-width="1.2"/>
        </svg>
        <span>0541762908</span>
      </p>
      <p class="contact__row">
        <svg class="contact__icon" viewBox="0 0 14 14" aria-hidden="true">
          <rect x="1" y="3" width="12" height="8" fill="var(--name-green)"/>
          <polyline points="1,3 7,8 13,3" fill="none" stroke="#ffffff" stroke-width="1"/>
        </svg>
        <span>tsabarieliran@mailvent.net</span>
      </p>
    </div>
  </section>
</main>
</body>
</html>
```